Cardiology practice business card

We need a business card for our cardiology practice "Bellmoor Cardiology". We have a new logo, attached below. We like the colours in the logo - red and charcoal. The front of the business card will need to have the doctors name, address, phone number and email. The back will need to have space to write 2 appointment dates and times.

```html
<!DOCTYPE html>
<html lang="en">
<head>
<meta charset="utf-8">
<title>Bellmoor Cardiology – Business Card</title>
<link href="https://fonts.googleapis.com/css2?family=Roboto:wght@300;400;700&display=swap" rel="stylesheet">
<style>
  :root {
    --backdrop: #778086;
    --card-red: #e92d29;
    --card-red-deep: #d3231f;
    --brand-red: #c9302c;
    --charcoal: #3f4245;
    --white: #ffffff;
    --rule: #a9a9a9;
    --watermark: #f3e9e4;
  }
  * { margin: 0; padding: 0; box-sizing: border-box; }
  html, body { width: 1200px; height: 1000px; overflow: hidden; }
  body {
    position: relative;
    background: var(--backdrop);
    font-family: "Roboto", Arial, sans-serif;
  }
  .card {
    position: absolute;
    left: 293px;
    width: 615px;
    height: 354px;
    border-radius: 18px;
    overflow: hidden;
  }
  .card--front { top: 68px; background: var(--card-red); color: var(--white); }
  .card--back { top: 471px; background: var(--white); }

  .heart-decoration {
    position: absolute;
    left: 307px;
    top: 0;
    width: 308px;
    height: 354px;
    border-radius: 140px 0 0 0;
  }
  .card--front .heart-decoration {
    background: radial-gradient(ellipse at 60% 45%, var(--card-red) 0%, var(--card-red) 55%, var(--card-red-deep) 100%);
  }
  .card--back .heart-decoration {
    background: radial-gradient(ellipse at 60% 45%, var(--white) 0%, var(--white) 50%, var(--watermark) 100%);
  }

  .brand-name {
    position: absolute;
    width: 195px;
    font-weight: 700;
    font-size: 24px;
    line-height: 26px;
    letter-spacing: 0.5px;
    white-space: nowrap;
    text-transform: uppercase;
    display: flex;
    flex-wrap: wrap;
    justify-content: center;
    align-items: center;
    gap: 0 8px;
    z-index: 1;
  }
  .brand-name__dot { width: 14px; height: 14px; border-radius: 50%; }
  .card--front .brand-name { left: 70px; top: 70px; }
  .card--front .brand-name__dot { background: var(--white); }
  .card--back .brand-name { left: 56px; top: 38px; color: var(--charcoal); }
  .card--back .brand-name__dot { background: var(--brand-red); }

  .contact {
    position: absolute;
    left: 40px;
    top: 156px;
    width: 255px;
    text-align: center;
    z-index: 1;
  }
  .contact__name { font-size: 23px; font-weight: 700; letter-spacing: 0.3px; line-height: 28px; }
  .contact__icons { display: flex; justify-content: center; gap: 4px; margin-top: 13px; }
  .contact__icon {
    width: 22px; height: 22px; border-radius: 50%;
    background: var(--white);
    display: flex; align-items: center; justify-content: center;
  }
  .contact__details { margin-top: 15px; font-size: 16px; font-weight: 300; line-height: 19.5px; }

  .appointment-title {
    position: absolute;
    left: 300px; top: 50px; width: 262px;
    text-align: center;
    color: var(--brand-red);
    font-size: 16px; font-weight: 700; letter-spacing: 0.3px;
    z-index: 1;
  }
  .appointment-table {
    position: absolute;
    left: 41px; top: 142px; width: 534px;
    border-collapse: collapse;
    z-index: 1;
  }
  .appointment-table th,
  .appointment-table td {
    border-top: 1.5px solid var(--rule);
    border-bottom: 1.5px solid var(--rule);
  }
  .appointment-table th + th,
  .appointment-table td + td { border-left: 1.5px solid var(--rule); }
  .appointment-table th {
    height: 40px;
    color: var(--brand-red);
    font-size: 16px; font-weight: 700;
  }
  .appointment-table th:first-child { padding-right: 44px; }
  .appointment-table th:last-child { padding-right: 20px; }
  .appointment-table th:first-child, .appointment-table td:first-child { width: 267px; }
  .appointment-table td { height: 43px; }
  .appointment-table tr:last-child td { height: 49px; }
</style>
</head>
<body>
  <section class="card card--front">
    <div class="heart-decoration" role="img" aria-label="Large heart outline with heartbeat line, tone on tone red"></div>
    <div class="brand-name"><span class="brand-name__dot"></span>Bellmoor<span>Cardiology</span></div>
    <div class="contact">
      <p class="contact__name">NAME SURNAME</p>
      <div class="contact__icons">
        <span class="contact__icon">
          <svg width="12" height="12" viewBox="0 0 24 24" aria-hidden="true"><path fill="#e92d29" d="M6.6 10.8a15.1 15.1 0 0 0 6.6 6.6l2.2-2.2c.3-.3.7-.4 1-.2 1.1.4 2.3.6 3.6.6.6 0 1 .4 1 1V20c0 .6-.4 1-1 1A17 17 0 0 1 3 4c0-.6.4-1 1-1h3.5c.6 0 1 .4 1 1 0 1.3.2 2.5.6 3.6.1.3 0 .7-.2 1z"/></svg>
        </span>
        <span class="contact__icon">
          <svg width="13" height="13" viewBox="0 0 24 24" aria-hidden="true"><rect x="2" y="5" width="20" height="14" rx="2" fill="#e92d29"/><path d="M3 6l9 7 9-7" fill="none" stroke="#fff" stroke-width="1.8"/></svg>
        </span>
        <span class="contact__icon">
          <svg width="12" height="12" viewBox="0 0 24 24" aria-hidden="true"><path fill="#e92d29" d="M12 2a7 7 0 0 0-7 7c0 5.2 7 13 7 13s7-7.8 7-13a7 7 0 0 0-7-7zm0 9.5A2.5 2.5 0 1 1 12 6.5a2.5 2.5 0 0 1 0 5z"/></svg>
        </span>
      </div>
      <p class="contact__details">(012) 345-6789<br>name@website.com<br>address</p>
    </div>
  </section>

  <section class="card card--back">
    <div class="heart-decoration" role="img" aria-label="Faint heart outline with heartbeat line watermark"></div>
    <div class="brand-name"><span class="brand-name__dot"></span>Bellmoor<span>Cardiology</span></div>
    <h2 class="appointment-title">YOUR NEXT APPOINTMENT</h2>
    <table class="appointment-table">
      <tr><th>DATE</th><th>TIME</th></tr>
      <tr><td></td><td></td></tr>
      <tr><td></td><td></td></tr>
      <tr><td></td><td></td></tr>
    </table>
  </section>
</body>
</html>
```